Business Card design needs editing

We have a business card design but I need to remove one of the providers. The provider to be removed is "Marlene Odgrave, Midwife.

Industry/Entity Type

Business

Contact Information for Business Card

I have uploaded a copy of our current business card

```html
<!DOCTYPE html>
<html lang="en">
<head>
<meta charset="utf-8">
<title>Bright Path Women's Health – Business Card</title>
<link href="https://fonts.googleapis.com/css2?family=Open+Sans:wght@400;600&family=Questrial&family=Tinos:wght@700&display=swap" rel="stylesheet">
<style>
  :root {
    --backdrop: #cfcfcf;
    --paper: #ffffff;
    --sky: #83c1d4;
    --ink: #111111;
    --slate: #7a7a7c;
  }
  html, body {
    margin: 0;
    width: 1189px;
    height: 1200px;
    overflow: hidden;
    background: var(--backdrop);
  }
  .card {
    position: absolute;
    left: 194px;
    width: 807px;
    height: 460px;
    background: var(--paper);
    overflow: hidden;
  }
  .card--front { top: 111px; }
  .card--back { top: 620px; }
  .card svg { position: absolute; left: 0; top: 0; }

  .brand-mark {
    position: absolute;
    left: 68px;
    top: 48px;
    width: 104px;
    height: 104px;
    border-radius: 50%;
    background: var(--sky);
  }
  .brand-name {
    position: absolute;
    left: 206px;
    top: 76px;
    margin: 0;
    font: 600 23px/1 "Open Sans", sans-serif;
    color: var(--sky);
    letter-spacing: 0.2px;
    white-space: nowrap;
  }
  .brand-tagline {
    position: absolute;
    left: 206px;
    top: 110px;
    margin: 0;
    font: 400 28px/1 "Questrial", sans-serif;
    color: var(--slate);
    white-space: nowrap;
  }

  .contact {
    position: absolute;
    left: 59px;
    top: 285px;
    font: 400 19px/1 "Open Sans", sans-serif;
    color: var(--ink);
  }
  .contact address { font-style: normal; line-height: 25px; margin: 0 0 10px; }
  .contact-line {
    display: flex;
    align-items: center;
    gap: 12px;
    height: 27px;
  }
  .contact-line svg { position: static; width: 16px; height: 16px; }

  .providers {
    position: absolute;
    right: 45px;
    top: 292px;
    margin: 0;
    padding: 0;
    list-style: none;
    text-align: right;
    font: 700 24px/33px "Tinos", serif;
    color: var(--ink);
  }

  .back-mark {
    position: absolute;
    left: 431px;
    top: 128px;
    width: 104px;
    height: 104px;
    border-radius: 50%;
    background: var(--sky);
  }
  .back-name {
    position: absolute;
    left: 0;
    width: 966px;
    top: 252px;
    margin: 0;
    text-align: center;
    font: 600 23px/1 "Open Sans", sans-serif;
    color: var(--sky);
  }
  .back-web {
    position: absolute;
    left: 232px;
    width: 486px;
    top: 342px;
    display: flex;
    align-items: center;
    gap: 10px;
    font: 600 31px/1 "Open Sans", sans-serif;
    color: var(--ink);
    white-space: nowrap;
  }
  .back-web .rule { flex: 1; height: 2px; background: var(--sky); }
</style>
</head>
<body>

<section class="card card--front">
  <svg width="807" height="460" viewBox="0 0 807 460" aria-hidden="true">
    <path class="wave-fill" fill="#83c1d4"
      d="M0 203 C70 250 150 285 240 285 C420 285 560 150 807 142 L807 460 L0 460 Z"/>
    <path class="wave-gap" fill="#ffffff"
      d="M0 196 C90 250 170 268 250 266 C420 262 560 170 807 134 L807 142 C560 150 420 285 240 285 C150 285 70 250 0 203 Z"/>
    <path class="wave-accent" fill="#83c1d4"
      d="M66 195 C180 250 320 262 440 236 C560 210 660 140 781 128 C650 150 560 220 440 246 C320 272 180 258 66 195 Z"/>
    <path class="wave-swoosh" fill="#111111"
      d="M0 171 C100 225 230 250 410 246 C250 272 110 262 0 196 Z"/>
  </svg>

  <span class="brand-mark" aria-hidden="true"></span>
  <h1 class="brand-name">BRIGHT PATH WOMEN'S HEALTH</h1>
  <p class="brand-tagline">Obstetrics &amp; Gynecology</p>

  <div class="contact">
    <address>2470 Larkspur Ave, Ste 3B<br>Fairview, GA 30555-1420</address>
    <div class="contact-line">
      <svg viewBox="0 0 16 16" aria-label="Phone"><path fill="#111" d="M1 6 C1 3 4 2 8 2 C12 2 15 3 15 6 L11 6 L11 4.5 C9 4 7 4 5 4.5 L5 6 Z M3 7 H13 L14 14 H2 Z"/></svg>
      <span>555-010-2746</span>
    </div>
    <div class="contact-line">
      <svg viewBox="0 0 16 16" aria-label="Fax"><rect x="4" y="1" width="8" height="5" fill="#111"/><rect x="1" y="6" width="14" height="6" rx="1" fill="#111"/><rect x="4" y="10" width="8" height="5" fill="#111" stroke="#83c1d4" stroke-width="1"/></svg>
      <span>555-010-3918</span>
    </div>
    <div class="contact-line">
      <svg viewBox="0 0 16 16" aria-label="Website"><circle cx="8" cy="8" r="6.5" fill="none" stroke="#111" stroke-width="1.3"/><ellipse cx="8" cy="8" rx="3" ry="6.5" fill="none" stroke="#111" stroke-width="1"/><path d="M1.5 8 H14.5 M2.5 5 H13.5 M2.5 11 H13.5" stroke="#111" stroke-width="1"/></svg>
      <span>www.brightpathobgyn.com</span>
    </div>
  </div>

  <ul class="providers">
    <li>Alicia Merrow, MD</li>
    <li>Dana Whitcombe, MD</li>
    <li>Nora Pellham, MD</li>
    <li>Rachel Tindall, Midwife</li>
  </ul>
</section>

<section class="card card--back">
  <span class="back-mark" aria-hidden="true"></span>
  <p class="back-name">BRIGHT PATH WOMEN'S HEALTH</p>
  <div class="back-web">
    <span class="rule"></span>
    <span>www.brightpathobgyn.com</span>
    <span class="rule"></span>
  </div>
</section>

</body>
</html>
```